Optometrist/Eye Care Clinic Business card with new logo attached

We are a small, independent eye care clinic in Canada. We have recently updated our logo (as attached), and would like a professional, modern and health care oriented business card to highlight our office details and our optometrist. We'd like to incorporate the blue colours as seen on our logo.

Target Market(s)

demographic: age 35-65 male/female equal

Industry/Entity Type

Health Care

Contact Information for Business Card

Name of clinic: "Marrow Bend Eye Care Optometry"

Font styles to use
Sans Serif

Colors
0355a3

Requirements
Must have
• our website: marrowbendeyecare.com
• Dr Lena Quorvik
• Optometrist
• 217-392 E Halvering Ave
• Vancouver BC V6R 3J8
• P: 604-319-2058
• E: info@marrowbendeyecare.com
Nice to have
• front side: logo/name of clinic as seen on logo attached and website
• backside: logo on the left side, and name/title/address/phone/email

```html
<!DOCTYPE html>
<html lang="en">
<head>
<meta charset="utf-8">
<title>Marrow Bend Eye Care Optometry – Business Card</title>
<link href="https://fonts.googleapis.com/css2?family=Poppins:wght@400;500;600&display=swap" rel="stylesheet">
<style>
  :root {
    --brand-blue: #0355a3;
    --brand-blue-light: #1a6fc9;
    --ink: #3a3f47;
    --paper: #ffffff;
    --stage: #e9ecf0;
  }
  * { box-sizing: border-box; margin: 0; padding: 0; }
  html, body { width: 1200px; height: 900px; overflow: hidden; }
  body {
    background: var(--stage);
    font-family: "Poppins", sans-serif;
    display: flex;
    flex-direction: column;
    align-items: center;
    justify-content: center;
    gap: 56px;
  }
  .card {
    width: 660px;
    height: 378px;
    border-radius: 22px;
    position: relative;
    overflow: hidden;
    box-shadow: 0 8px 24px rgba(0,0,0,0.12);
  }

  /* Front */
  .card-front {
    background: linear-gradient(160deg, var(--brand-blue-light) 0%, var(--brand-blue) 100%);
    color: var(--paper);
    display: flex;
    flex-direction: column;
    align-items: center;
    justify-content: center;
    text-align: center;
  }
  .front-mark {
    width: 92px; height: 92px;
    border-radius: 50%;
    border: 12px solid var(--paper);
    margin-bottom: 22px;
  }
  .front-name {
    font-weight: 500;
    font-size: 26px;
    line-height: 1.25;
    letter-spacing: 0.14em;
    text-transform: uppercase;
    color: var(--paper);
  }
  .front-website {
    margin-top: 34px;
    font-weight: 600;
    font-size: 15px;
    letter-spacing: 0.02em;
  }

  /* Back */
  .card-back {
    background: var(--paper);
    color: var(--ink);
  }
  .back-clinic {
    position: absolute;
    left: 48px; top: 52px;
    font-weight: 500;
    font-size: 21px;
    line-height: 1.3;
    letter-spacing: 0.14em;
    text-transform: uppercase;
    color: var(--brand-blue);
    width: 300px;
  }
  .back-address {
    position: absolute;
    left: 48px; top: 206px;
    font-size: 14px;
    line-height: 1.45;
    font-style: normal;
  }
  .back-contacts {
    position: absolute;
    left: 48px; top: 270px;
    list-style: none;
    font-size: 14px;
    line-height: 1.55;
  }
  .back-contacts li { display: flex; align-items: center; gap: 10px; }
  .back-contacts svg { width: 13px; height: 13px; fill: none; stroke: var(--brand-blue); stroke-width: 2; }
  .doctor {
    position: absolute;
    right: 52px; top: 150px;
    text-align: right;
  }
  .doctor-name {
    font-weight: 600;
    font-size: 24px;
    letter-spacing: 0.04em;
    color: var(--brand-blue);
    text-transform: uppercase;
  }
  .doctor-title {
    font-weight: 500;
    font-size: 15px;
    color: var(--ink);
  }
  .edge-accent {
    position: absolute;
    right: 0; top: 140px;
    width: 10px; height: 62px;
    background: var(--brand-blue);
  }
</style>
</head>
<body>

  <section class="card card-front">
    <div class="front-mark"></div>
    <h1 class="front-name">Marrow Bend<br>Eye Care<br>Optometry</h1>
    <p class="front-website">www.marrowbendeyecare.com</p>
  </section>

  <section class="card card-back">
    <h2 class="back-clinic">Marrow Bend Eye Care Optometry</h2>

    <address class="back-address">
      217-392 E Halvering Ave<br>
      Vancouver BC V6R 3J8
    </address>

    <ul class="back-contacts">
      <li>
        <svg viewBox="0 0 24 24"><path d="M5 3h4l2 5-2.5 1.5a11 11 0 0 0 6 6L16 13l5 2v4a2 2 0 0 1-2 2A17 17 0 0 1 3 5a2 2 0 0 1 2-2z"/></svg>
        604-319-2058
      </li>
      <li>
        <svg viewBox="0 0 24 24"><rect x="3" y="5" width="18" height="14" rx="1"/><path d="M3 6l9 7 9-7"/></svg>
        info@marrowbendeyecare.com
      </li>
      <li>
        <svg viewBox="0 0 24 24"><circle cx="12" cy="12" r="9"/><path d="M3 12h18M12 3c3 3 3 15 0 18M12 3c-3 3-3 15 0 18"/></svg>
        marrowbendeyecare.com
      </li>
    </ul>

    <div class="doctor">
      <p class="doctor-name">Dr. Lena Quorvik</p>
      <p class="doctor-title">Optometrist</p>
    </div>
    <div class="edge-accent"></div>
  </section>

</body>
</html>
```